A Weather Forecasting Site needs designs

We need a website design for our new venture which is a weather forecasting website. This website should have the latest design trends.

Menu
Weather, Maps, Videos and Photos

The home page requirements are as follows:
- Search Bar
- Local Weather
- Weather forecast of major cities in the World
Favorite locations
- Space for ADs
- Email signup

Weather Details page
This page will be redirected from the home page when you click on any of the weather forecast section

We are open to all kinds of designs and ideas. Feel free to you colors which suite your design.

```html
<!DOCTYPE html>
<html lang="en">
<head>
<meta charset="utf-8">
<title>Skycast — Weather Forecast</title>
<link href="https://fonts.googleapis.com/css2?family=Montserrat:wght@300;400;500;600;700&display=swap" rel="stylesheet">
<style>
:root{
  --dark:#2b2e36;
  --darker:#23252b;
  --red:#e54c3c;
  --blue:#2a7fc4;
  --sky:#4f8fd0;
  --panel:#f4f4f4;
  --text:#333;
  --muted:#888;
  --white:#fff;
}
*{box-sizing:border-box;margin:0;padding:0}
html,body{width:1200px;height:2219px;overflow:hidden}
body{font-family:'Montserrat',sans-serif;color:var(--text);background:var(--white);position:relative}
.abs{position:absolute}
.wrap{position:absolute;left:147px;width:905px}

/* top navigation */
.topbar{position:absolute;left:0;top:0;width:1200px;height:77px;background:var(--darker)}
.main-nav{top:0;height:95px;background:var(--dark);display:flex}
.main-nav::before{content:"";position:absolute;left:0;top:0;width:905px;height:6px;background:linear-gradient(90deg,var(--red) 0 152px,var(--blue) 152px)}
.main-nav a{flex:1;display:flex;align-items:center;justify-content:center;color:var(--white);font-size:12px;font-weight:600;text-decoration:none;text-transform:uppercase;border-right:1px solid #383b44;padding-top:6px}
.main-nav a:last-child{border:none}

/* header */
.brand{top:136px;display:flex;align-items:center;gap:12px}
.brand-mark{width:40px;height:40px;border-radius:50%;background:var(--red)}
.brand-name{font-size:38px;font-weight:400;color:var(--dark);letter-spacing:-0.5px}
.account{top:136px;left:743px;width:207px;height:46px;background:var(--dark);color:var(--white);font-size:12px;font-weight:600;display:flex;align-items:center;justify-content:center;gap:10px}
.login{top:136px;left:950px;width:102px;height:46px;background:var(--red);color:var(--white);font-size:12px;font-weight:600;display:flex;align-items:center;justify-content:center;gap:8px}

/* hero */
.hero-photo{top:292px;left:0;width:1200px;height:444px;background:linear-gradient(180deg,#3f6e7e 0%,#86a9b0 35%,#b7c6c0 55%,#8a8f6f 78%,#a48a3c 100%)}
.search{top:229px;height:86px;background:#ececec;box-shadow:0 2px 6px rgba(0,0,0,.25);z-index:2}
.search-input{position:absolute;left:20px;top:27px;width:712px;height:36px;background:var(--white);font-size:10px;color:#999;padding:12px 16px;text-transform:uppercase}
.search-btn{position:absolute;left:737px;top:27px;width:36px;height:36px;background:var(--blue);display:flex;align-items:center;justify-content:center}
.unit{position:absolute;top:27px;width:37px;height:36px;color:var(--white);font-size:15px;display:flex;align-items:center;justify-content:center}
.unit.c{left:794px;background:var(--dark)}
.unit.f{left:849px;background:var(--red)}
.now{top:545px;height:191px;background:rgba(80,90,100,.55)}
.now .icon{position:absolute;left:205px;top:30px}
.now .readings{position:absolute;left:420px;top:60px;color:var(--white);font-size:28px;font-weight:300;display:flex;gap:24px}
.now .city{position:absolute;left:400px;top:100px;width:310px;text-align:center;color:var(--white)}
.now .city b{display:block;font-size:44px;font-weight:700;line-height:1}
.now .city span{font-size:20px}
.arrow{position:absolute;top:80px;color:var(--red);font-size:26px}
.forecast{top:736px;height:124px;background:var(--red);display:flex}
.day{flex:1;border-right:1px solid #d23f30;color:var(--white);text-align:center;padding-top:16px}
.day:last-child{border:none}
.day h4{font-size:16px;font-weight:600}
.day .t{font-size:15px;font-weight:500;margin-top:4px}

/* local weather */
.local h2{font-size:31px;font-weight:600;color:var(--dark)}
.local small{display:block;font-size:9px;color:#666;margin-top:4px}
.card{top:998px;height:220px}
.card-photo{position:absolute;left:0;top:0;width:223px;height:195px;background:linear-gradient(180deg,#5f7fb8,#34456e 60%,#6a6a74)}
.card-sky{position:absolute;left:223px;top:0;width:153px;height:195px;background:#2f5ea6}
.card-sky .temp{position:absolute;left:20px;top:128px;color:var(--white);font-size:36px;font-weight:500}
.card-sky .temp sup{font-size:12px;vertical-align:super}
.card-sky .mm{position:absolute;left:20px;top:140px;color:var(--white);font-size:11px;line-height:1.2}
.card-bar{position:absolute;left:0;top:195px;width:376px;height:25px;background:var(--sky);color:var(--white);font-size:12px;display:flex;justify-content:space-between;align-items:center;padding:0 20px}
.card-bar b{font-weight:600}
.next{top:1230px;width:376px;display:flex}
.next div{flex:1;padding-left:28px;position:relative}
.next h5{font-size:14px;font-weight:600}
.next .v{font-size:26px;font-weight:300;margin-left:50px;margin-top:4px}
.next .mm{position:absolute;left:78px;top:28px;font-size:9px;line-height:1.2}
.next .rain{font-size:10px;color:#aaa;margin-left:88px}
.next svg{position:absolute;left:32px;top:28px}
.stats{top:1332px;width:376px}
.stats div{height:35px;display:flex;align-items:center;font-size:17px;font-weight:300;padding-left:0}
.stats div:nth-child(odd){background:var(--panel)}
.stats span{width:272px}
.stats em{font-style:normal;color:#777}
.btn-red{top:1572px;width:162px;height:37px;background:var(--red);color:var(--white);font-size:11px;font-weight:700;display:flex;align-items:center;justify-content:center}

/* favourites */
.fav{top:915px;left:576px;width:476px;height:695px;background:var(--panel);padding:0 30px}
.fav h3{position:absolute;left:30px;top:30px;font-size:20px;font-weight:500;color:var(--dark)}
.fav .pager{position:absolute;left:392px;top:26px;display:flex}
.fav .pager i{width:29px;height:29px;display:flex;align-items:center;justify-content:center;color:var(--white);font-style:normal;font-size:14px}
.item{position:absolute;left:30px;width:416px;height:104px}
.item::after{content:"";position:absolute;left:0;right:0;bottom:-24px;height:1px;background:#ddd}
.item:last-child::after{display:none}
.thumb{position:absolute;left:0;top:0;width:194px;height:104px;border-radius:3px}
.item h6{position:absolute;left:212px;top:4px;font-size:14px;font-weight:600}
.item p{position:absolute;left:212px;top:28px;width:200px;font-size:11.5px;line-height:1.55;color:#555}
.item a{position:absolute;left:212px;top:80px;font-size:10px;font-weight:700;color:var(--red);text-decoration:none}

/* ad + newsletter */
.ad{top:1693px;height:136px;background:linear-gradient(180deg,#6d7270,#8c9a78 45%,#4f6e2f);display:flex;align-items:center;justify-content:center;gap:14px}
.ad b{display:block;font-size:42px;font-weight:700;color:var(--white);line-height:1}
.ad span{font-size:17px;font-weight:500;color:var(--red)}
.news{top:1863px;height:86px;background:var(--red);display:flex;align-items:center}
.news h3{font-size:26px;font-weight:300;color:var(--white);margin-left:100px}
.news h3 b{font-weight:700}
.news .field{margin-left:40px;width:316px;height:38px;border:1px solid var(--white);border-radius:4px;color:var(--white);font-size:12px;display:flex;align-items:center;justify-content:space-between;padding:0 14px}

/* footer */
.footer{position:absolute;left:0;top:2032px;width:1200px;height:138px;background:var(--dark)}
.foot-nav{position:absolute;left:147px;top:34px;width:905px;display:flex}
.foot-nav a{flex:1;text-align:center;color:#bbb;font-size:11px;text-decoration:none;border-right:1px solid #444}
.foot-nav a:last-child{border:none}
.social{position:absolute;left:543px;top:86px;display:flex;gap:5px}
.social i{width:31px;height:31px;background:var(--red);display:block}
.copy{position:absolute;left:0;top:2170px;width:1200px;height:49px;background:var(--darker);color:#888;font-size:10px;display:flex;align-items:center;justify-content:center}
</style>
</head>
<body>
<svg width="0" height="0" style="position:absolute">
  <defs>
    <symbol id="cloud" viewBox="0 0 40 26"><path d="M10 26a8 8 0 0 1-1-16 11 11 0 0 1 21 2 7 7 0 0 1 0 14z" fill="currentColor"/></symbol>
    <symbol id="sun" viewBox="0 0 40 40"><circle cx="20" cy="20" r="8" fill="none" stroke="currentColor" stroke-width="3"/><g stroke="currentColor" stroke-width="3" stroke-linecap="round"><path d="M20 2v6M20 32v6M2 20h6M32 20h6M7 7l4 4M29 29l4 4M33 7l-4 4M11 29l-4 4"/></g></symbol>
  </defs>
</svg>

<div class="topbar"></div>
<nav class="wrap main-nav">
  <a href="#">Home</a><a href="#">Weather</a><a href="#">Maps</a><a href="#">Videos</a><a href="#">Photos</a><a href="#">Contacts</a>
</nav>

<div class="wrap brand"><i class="brand-mark"></i><span class="brand-name">SKYCAST</span></div>
<div class="abs account">
  <svg width="10" height="11" viewBox="0 0 10 11"><circle cx="5" cy="3" r="2.5" fill="#fff"/><path d="M0 11a5 5 0 0 1 10 0z" fill="#fff"/></svg>OPEN AN ACCOUNT <span style="color:#777;margin-left:12px">▾</span>
</div>
<div class="abs login">
  <svg width="10" height="12" viewBox="0 0 10 12"><rect x="0" y="5" width="10" height="7" fill="#fff"/><path d="M2 5V3a3 3 0 0 1 6 0v2" stroke="#fff" stroke-width="1.6" fill="none"/></svg>LOGIN
</div>

<div class="abs hero-photo" role="img" aria-label="Sky with clouds and a hot air balloon over a field"></div>
<div class="wrap search">
  <div class="search-input">Search zip, city, or place...</div>
  <div class="search-btn"><svg width="16" height="16" viewBox="0 0 16 16"><circle cx="6.5" cy="6.5" r="5" fill="none" stroke="#fff" stroke-width="2"/><path d="M10 10l5 5" stroke="#fff" stroke-width="2.4"/></svg></div>
  <div class="unit c">C°</div>
  <div class="unit f">F°</div>
</div>

<section class="wrap now">
  <span class="arrow" style="left:22px">←</span>
  <span class="arrow" style="right:22px">→</span>
  <svg class="icon" width="120" height="130" viewBox="0 0 120 130" style="color:#fff">
    <use href="#sun" x="30" y="0" width="80" height="80"/>
    <use href="#cloud" x="0" y="45" width="120" height="80"/>
  </svg>
  <div class="readings"><span>🌡35°</span><span>☂29°</span></div>
  <div class="city"><b>Auckland</b><span>New Zealand</span></div>
</section>

<div class="wrap forecast">
  <div class="day"><h4>MON</h4><svg width="44" height="38" style="color:#fff"><use href="#cloud" x="2" y="4" width="40" height="26"/></svg><div class="t">31° &nbsp;25°</div></div>
  <div class="day"><h4>TUE</h4><svg width="44" height="38" style="color:#fff"><use href="#cloud" x="2" y="8" width="40" height="26"/></svg><div class="t">31° &nbsp;26°</div></div>
  <div class="day"><h4>WED</h4><svg width="44" height="38" style="color:#fff"><use href="#cloud" x="2" y="6" width="40" height="26"/></svg><div class="t">30° &nbsp;25°</div></div>
  <div class="day"><h4>THU</h4><svg width="44" height="38" style="color:#fff"><use href="#cloud" x="2" y="8" width="40" height="26"/></svg><div class="t">31° &nbsp;27°</div></div>
  <div class="day"><h4>FRI</h4><svg width="44" height="38" style="color:#fff"><use href="#cloud" x="2" y="6" width="40" height="26"/></svg><div class="t">29° &nbsp;25°</div></div>
  <div class="day"><h4>SAT</h4><svg width="44" height="38" style="color:#fff"><use href="#cloud" x="2" y="6" width="40" height="26"/></svg><div class="t">31° &nbsp;26°</div></div>
</div>

<section class="local">
  <div class="abs" style="left:147px;top:922px"><h2>Local Weather</h2><small>UPDATED 12.50 PM ET</small></div>
  <div class="abs card" style="left:147px;width:376px">
    <div class="card-photo" role="img" aria-label="Paris skyline at dusk"></div>
    <div class="card-sky">
      <svg style="position:absolute;left:22px;top:26px;color:#b9cbe6" width="100" height="70" viewBox="0 0 100 70"><path d="M22 64a16 16 0 0 1-2-32 24 24 0 0 1 44 4 14 14 0 0 1 4 28z" fill="none" stroke="currentColor" stroke-width="6"/><path d="M70 30a16 16 0 0 0 14-26 20 20 0 0 1-22 22" fill="none" stroke="currentColor" stroke-width="5"/></svg>
      <div class="mm">24<br>&nbsp;9</div>
      <div class="temp" style="left:44px">22<sup>o</sup> C</div>
    </div>
    <div class="card-bar"><b>Paris, France</b><span>Monday, September 30, 2017</span></div>
  </div>
  <div class="abs next" style="left:147px">
    <div><h5>Tuesday</h5><svg width="40" height="40" style="color:var(--red);left:-4px"><use href="#sun" width="40" height="40"/></svg><div class="mm" style="left:62px">25<br>12</div><div class="v">25<sup style="font-size:11px">0</sup> C</div><div class="rain">Rain: 0%</div></div>
    <div><h5>Wednesday</h5><svg width="44" height="44" style="color:var(--red);left:-4px"><use href="#cloud" x="2" y="8" width="40" height="26"/></svg><div class="mm" style="left:62px">18<br>&nbsp;8</div><div class="v">18<sup style="font-size:11px">0</sup> C</div><div class="rain">Rain: 80%</div></div>
  </div>
  <div class="abs stats" style="left:147px">
    <div><span>Feels like:</span><em>26°</em></div>
    <div><span>Humidity:</span><em>71%</em></div>
    <div><span>Wind:</span><em>S 10 mph</em></div>
    <div><span>Sunrise:</span><em>6:31 AM</em></div>
    <div><span>Sunset:</span><em>8:52 PM</em></div>
    <div><span>Barometer:</span><em>30.03" Hg</em></div>
  </div>
  <div class="abs btn-red" style="left:147px">CHANGE LOCATION &gt;&gt;</div>
</section>

<aside class="abs fav">
  <h3>Favourite Locations</h3>
  <div class="pager"><i style="background:var(--dark)">‹</i><i style="background:var(--red)">›</i></div>
  <div class="item" style="top:85px"><div class="thumb" role="img" aria-label="City skyline with a tall tower" style="background:linear-gradient(180deg,#8aa2bf,#5a6478)"></div><h6>City Name Goes Here</h6><p>Lorem ipsum dolor sit amet, consectetur adipisicing elit, sed.</p><a href="#">VIEW WEATHER &gt;&gt;</a></div>
  <div class="item" style="top:238px"><div class="thumb" role="img" aria-label="Harbour town at sunset" style="background:linear-gradient(180deg,#b0886a,#5a4a4e)"></div><h6>City Name Goes Here</h6><p>Lorem ipsum dolor sit amet, consectetur adipisicing elit, sed.</p><a href="#">VIEW WEATHER &gt;&gt;</a></div>
  <div class="item" style="top:393px"><div class="thumb" role="img" aria-label="Coastal city below mountains" style="background:linear-gradient(180deg,#4d7cc0,#2f4f7a)"></div><h6>City Name Goes Here</h6><p>Lorem ipsum dolor sit amet, consectetur adipisicing elit, sed.</p><a href="#">VIEW WEATHER &gt;&gt;</a></div>
  <div class="item" style="top:553px"><div class="thumb" role="img" aria-label="Modern glass dome building by the water" style="background:linear-gradient(180deg,#3f6fb0,#6e8a6a)"></div><h6>City Name Goes Here</h6><p>Lorem ipsum dolor sit amet, consectetur adipisicing elit, sed.</p><a href="#">VIEW WEATHER &gt;&gt;</a></div>
</aside>

<div class="wrap ad" role="img" aria-label="Advertising banner over green hills">
  <svg width="60" height="60" viewBox="0 0 60 60"><path d="M56 4C40 4 26 14 20 30l10 10C46 34 56 20 56 4z" fill="#fff"/><path d="M20 30l-10 2-6 10 12-2zM30 40l-2 10-10 6 2-12z" fill="#fff"/><path d="M14 46l-8 8" stroke="#fff" stroke-width="3"/></svg>
  <div><b>YOUR AD</b><span>Goes here...</span></div>
</div>

<div class="wrap news">
  <h3>Subscribe to our <b>Newsletter</b></h3>
  <div class="field">Your Email... <svg width="32" height="12" viewBox="0 0 32 12"><path d="M0 6h26M22 1l8 5-8 5" stroke="#fff" stroke-width="2.4" fill="none"/></svg></div>
</div>

<footer class="footer">
  <nav class="foot-nav"><a href="#">HOME</a><a href="#">WEATHER</a><a href="#">MAPS</a><a href="#">VIDEOS</a><a href="#">PHOTOS</a><a href="#">CONTACTS</a></nav>
  <div class="social"><i></i><i></i><i></i></div>
</footer>
<div class="copy">©COPYRIGHT 2017. ALL RIGHTS ARE RESERVED.</div>
</body>
</html>
```